Wow me with your Earring card options!

An A7 portrait sized earring card is required for Marble & Mango. Inspired by Marble and fueled by Mango we love our accessories to do the talking. Bold statement earrings are our thing. Our earring cards need to showcase our brand while not stealing all of the limelight from the earrings themselves. Earring care information needs to be included on the back side of the card. Our simple logo needs to be the basis for the colour choices used on the card.

Requirements
Should not have
• No florals please 😊

```html
<!DOCTYPE html>
<html lang="en">
<head>
<meta charset="utf-8">
<title>Marble &amp; Mango – Earring Card</title>
<link rel="stylesheet" href="https://fonts.googleapis.com/css2?family=Poppins:wght@400;500;700;800&display=swap">
<style>
  :root {
    --stage: #8a8a8a;
    --card: #050505;
    --card-glow: #1e1e1e;
    --white: #ffffff;
    --gold: #c9a45a;
    --gold-light: #e9c987;
    --gold-dark: #a9823c;
  }
  * { box-sizing: border-box; margin: 0; padding: 0; }
  html, body { width: 950px; height: 1200px; overflow: hidden; }
  body {
    background: var(--stage);
    font-family: "Poppins", sans-serif;
    color: var(--white);
    position: relative;
  }
  .card {
    position: absolute;
    top: 303px;
    width: 420px;
    height: 593px;
    background: radial-gradient(ellipse at 50% 12%, var(--card-glow) 0%, var(--card) 55%);
    box-shadow: 0 6px 18px rgba(0,0,0,.35);
    overflow: hidden;
  }
  .card--front { left: 35px; }
  .card--back { left: 495px; }

  /* front */
  .brand-name {
    position: absolute;
    top: 72px; left: 0; width: 100%;
    text-align: center;
    font-weight: 700;
    font-size: 30px;
    letter-spacing: 1px;
    color: var(--white);
  }
  .product-photo {
    position: absolute;
    top: 161px; left: 54px;
    width: 312px; height: 312px;
    border-radius: 50%;
    border: 2px solid var(--gold);
    background: radial-gradient(circle at 50% 45%, #3a3a3c 0%, #232325 55%, #151516 100%);
  }
  .front-url {
    position: absolute;
    top: 503px; left: 0; width: 100%;
    text-align: center;
    font-weight: 500;
    font-size: 16px;
    letter-spacing: .3px;
  }

  /* back */
  .care-title {
    position: absolute;
    top: 28px; left: 48px; width: 324px;
    font-weight: 800;
    font-size: 72px;
    line-height: 1;
    letter-spacing: -1px;
    text-align: center;
    color: var(--white);
  }
  .care-subtitle {
    position: absolute;
    top: 101px; left: 49px;
    width: 323px; height: 36px;
    border: 1.5px solid var(--white);
    text-align: center;
    line-height: 33px;
    font-size: 17px;
    font-weight: 500;
    letter-spacing: 5px;
  }
  .care-list { list-style: none; }
  .care-item {
    position: absolute;
    left: 50px; width: 340px; height: 58px;
    display: flex; align-items: center;
  }
  .care-item:nth-child(1) { top: 164px; }
  .care-item:nth-child(2) { top: 238px; }
  .care-item:nth-child(3) { top: 314px; }
  .care-item:nth-child(4) { top: 387px; }
  .care-icon { width: 58px; height: 58px; flex: none; }
  .care-text {
    margin-left: 30px;
    font-size: 16px;
    line-height: 1.22;
  }
  .contact-box {
    position: absolute;
    top: 467px; left: 15px;
    width: 390px; height: 110px;
    border: 1px solid var(--gold);
  }
  .contact-list { list-style: none; position: absolute; left: 17px; top: 19px; }
  .contact-item {
    display: flex; align-items: center;
    height: 23px;
    font-size: 13px;
  }
  .contact-icon {
    width: 17px; height: 16px;
    margin-right: 19px;
    border-radius: 3px;
    background: linear-gradient(135deg, var(--gold-light), var(--gold-dark));
  }
  .social-tile {
    position: absolute;
    top: 19px; left: 293px;
    width: 77px; height: 68px;
    border-radius: 4px;
    background: linear-gradient(135deg, var(--gold-light), var(--gold-dark));
  }
</style>
</head>
<body>

<section class="card card--front">
  <h1 class="brand-name">Marble &amp; Mango</h1>
  <div class="product-photo" role="img" aria-label="Product photo: pair of silver statement drop earrings with blue stones on dark textured stone"></div>
  <p class="front-url">www.marbleandmango.com.au</p>
</section>

<section class="card card--back">
  <h2 class="care-title">EARNING</h2>
  <p class="care-subtitle">CARE INSTRUCTION</p>

  <svg width="0" height="0" style="position:absolute" aria-hidden="true">
    <defs>
      <linearGradient id="ring-spectrum" x1="0" y1="0" x2="1" y2="1">
        <stop offset="0" stop-color="#6cc04a"/>
        <stop offset=".3" stop-color="#ffd93b"/>
        <stop offset=".55" stop-color="#ff6a13"/>
        <stop offset=".75" stop-color="#ec2a8a"/>
        <stop offset="1" stop-color="#6a1bf2"/>
      </linearGradient>
    </defs>
  </svg>

  <ul class="care-list">
    <li class="care-item">
      <svg class="care-icon" viewBox="0 0 58 58" aria-hidden="true">
        <circle cx="29" cy="29" r="27" fill="none" stroke="url(#ring-spectrum)" stroke-width="2"/>
        <g fill="none" stroke="#fff" stroke-width="1.4" stroke-linejoin="round">
          <rect x="24" y="14" width="6" height="6"/>
          <rect x="18" y="20" width="18" height="20" rx="5"/>
          <line x1="18" y1="28" x2="36" y2="28"/>
          <circle cx="39" cy="31" r="5"/>
        </g>
      </svg>
      <span class="care-text">Avoid moisture &amp; remove<br>before bathing</span>
    </li>
    <li class="care-item">
      <svg class="care-icon" viewBox="0 0 58 58" aria-hidden="true">
        <circle cx="29" cy="29" r="27" fill="none" stroke="url(#ring-spectrum)" stroke-width="2"/>
        <g fill="none" stroke="#fff" stroke-width="1.4" stroke-linejoin="round">
          <rect x="15" y="20" width="28" height="10" rx="2"/>
          <rect x="19" y="23" width="8" height="5" rx="1"/>
          <rect x="31" y="23" width="8" height="5" rx="1"/>
          <rect x="13" y="30" width="32" height="7" rx="1"/>
          <line x1="15" y1="37" x2="15" y2="40"/>
          <line x1="43" y1="37" x2="43" y2="40"/>
        </g>
      </svg>
      <span class="care-text">For comforts sake, remove<br>before bed!</span>
    </li>
    <li class="care-item">
      <svg class="care-icon" viewBox="0 0 58 58" aria-hidden="true">
        <circle cx="29" cy="29" r="27" fill="none" stroke="url(#ring-spectrum)" stroke-width="2"/>
        <g fill="none" stroke="#fff" stroke-width="1.3" stroke-linecap="round">
          <path d="M19 30 l5 -12 M25 30 l5 -12 M31 30 l5 -12 M37 30 l5 -12"/>
          <line x1="16" y1="32" x2="42" y2="32"/>
          <circle cx="19" cy="39" r="2.5"/><circle cx="26" cy="39" r="2.5"/>
          <circle cx="33" cy="39" r="2.5"/><circle cx="40" cy="39" r="2.5"/>
        </g>
      </svg>
      <span class="care-text">Avoid contact with<br>perfumes &amp; lotions</span>
    </li>
    <li class="care-item">
      <svg class="care-icon" viewBox="0 0 58 58" aria-hidden="true">
        <circle cx="29" cy="29" r="27" fill="none" stroke="url(#ring-spectrum)" stroke-width="2"/>
        <g fill="none" stroke="#fff" stroke-width="1.5" stroke-linecap="round">
          <circle cx="29" cy="29" r="7"/>
          <path d="M29 14v4 M29 40v4 M14 29h4 M40 29h4 M18.4 18.4l2.8 2.8 M36.8 36.8l2.8 2.8 M18.4 39.6l2.8-2.8 M36.8 21.2l2.8-2.8"/>
        </g>
      </svg>
      <span class="care-text">Store away from direct<br>sunlight</span>
    </li>
  </ul>

  <div class="contact-box">
    <ul class="contact-list">
      <li class="contact-item"><span class="contact-icon"></span>www.marbleandmango.com.au</li>
      <li class="contact-item"><span class="contact-icon"></span>hello@marbleandmango.com.au</li>
      <li class="contact-item"><span class="contact-icon"></span>@marbleandmango</li>
    </ul>
    <svg class="social-tile" viewBox="0 0 77 68" aria-label="Social channels">
      <line x1="38.5" y1="6" x2="38.5" y2="62" stroke="#3a2a10" stroke-width=".8"/>
      <line x1="6" y1="34" x2="71" y2="34" stroke="#3a2a10" stroke-width=".8"/>
      <circle cx="21" cy="18" r="6" fill="#111"/>
      <circle cx="56" cy="18" r="6" fill="#111"/>
      <circle cx="21" cy="50" r="6" fill="#111"/>
      <circle cx="56" cy="50" r="6" fill="#111"/>
    </svg>
  </div>
</section>

</body>
</html>
```